Real Estate Agent "Team" Ad that will go into the local newspaper

We need an ad design for the local newspaper. I've attached a copy of our last ad. We would like a little different design (use same content). The size is 4 inches tall x 6.5 inches wide. We would like to include our two photos. Keep it CLEAN and simple. We are a Mercer Island, Washington-based mother/daughter Ridgeway Harlan real estate team focused exclusively on Mercer Island. The graphic design should reinforce the tone of warm/approachable, while clean and polished. The feel should be on-trend, current and clean/tight/contemporary. Should appeal to a high net worth consumer. The design should tell potential clients that Greta & Nora are the premier, trusted team of advisors that informed buyers and sellers turn to for any residential real estate opportunities on Mercer Island.

Target Market(s)

Mercer Island Residents (past and potential customers). High-end, sophisticated Buyers.

Industry/Entity Type

Real Estate Agent

Font styles to use
Serif
Sans Serif

Colors
959595
5c5c5c
474747

Requirements
Must have
• Greta Loxley and Nora Loxley Photos. Personal Logo. Ridgeway Harlan Teague logo. Please keep colors simple (Black and White) with the exception of our photos and logos.
Nice to have
• Please keep Greta and Nora Photos equal in size. This is a partnership.
Should not have
• No additional photos of houses or keys.

```html
<!DOCTYPE html>
<html lang="en">
<head>
<meta charset="utf-8">
<title>Greta Loxley &amp; Nora Loxley Marsh Real Estate – Newspaper Ad</title>
<link rel="stylesheet" href="https://fonts.googleapis.com/css2?family=Jost:ital,wght@0,400;0,500;1,400&display=swap">
<style>
  :root {
    --page: #f2f2f2;
    --frame: #5c5c5c;
    --band: #5c5c5c;
    --logo-grey: #8c8c8c;
    --ink: #111111;
    --lime: #9cc13a;
    --panel-top: #e4e4e4;
    --panel-bottom: #cfcfcf;
    --white: #ffffff;
  }
  * { box-sizing: border-box; margin: 0; padding: 0; }
  html, body {
    width: 1200px; height: 1200px; overflow: hidden;
    background: var(--page);
    font-family: "Jost", "Helvetica Neue", Arial, sans-serif;
  }
  .ad {
    position: absolute; left: 288px; top: 93px;
    width: 624px; height: 1015px;
    background: var(--frame);
    box-shadow: 6px 8px 10px rgba(0,0,0,0.25);
  }
  .ad-inner {
    position: absolute; left: 12px; top: 11px; width: 601px; height: 992px;
    background: linear-gradient(180deg, #ffffff 0%, #ffffff 22%, #ececec 42%, #ebebeb 60%);
    overflow: hidden;
  }
  .brand-mark {
    position: absolute; left: 47px; top: 40px;
    width: 107px; height: 130px; background: var(--lime);
  }
  .brand-name {
    position: absolute; left: 170px; top: 42px; width: 370px;
    color: var(--logo-grey); font-weight: 500; text-transform: uppercase;
    line-height: 1;
  }
  .brand-name .line { display: block; font-size: 36px; letter-spacing: -0.5px; white-space: nowrap; }
  .brand-name .line + .line { margin-top: 14px; }
  .brand-name .rule { display: block; height: 2px; background: var(--logo-grey); margin: 10px 0 8px; width: 367px; }
  .brand-name .sub { display: block; font-size: 17px; letter-spacing: 19px; white-space: nowrap; }

  .headline {
    position: absolute; left: 0; right: 0; top: 212px; text-align: center; color: var(--ink);
  }
  .headline .lead { font-size: 35px; font-weight: 400; letter-spacing: -0.5px; line-height: 42px; }
  .headline .tag { font-size: 31px; font-style: italic; line-height: 40px; }

  .portrait {
    position: absolute; top: 321px; width: 271px; height: 298px;
    border: 3px solid var(--lime);
    background: linear-gradient(180deg, #ffffff 0%, #f2f2f2 45%, #3a3a3a 100%);
  }
  .portrait.nora { left: 23px; }
  .portrait.greta { left: 301px; background: linear-gradient(180deg, #ffffff 0%, #eeeeee 45%, #4a4a4a 100%); }

  .contact-band {
    position: absolute; left: 0; right: 0; top: 619px; height: 75px;
    background: var(--band); color: var(--white);
  }
  .agent {
    position: absolute; top: 10px; width: 271px; text-align: center;
    font-size: 22px; line-height: 27px;
  }
  .agent.nora { left: 23px; }
  .agent.greta { left: 301px; }

  .info-panel {
    position: absolute; left: 0; right: 0; top: 694px; bottom: 16px;
    background: linear-gradient(180deg, var(--panel-top), var(--panel-bottom));
  }
  .promise {
    position: absolute; left: 0; right: 0; top: 40px; text-align: center;
    font-size: 28px; line-height: 36px; color: var(--ink); letter-spacing: -0.3px;
  }
  .broker-badge {
    position: absolute; left: 23px; top: 160px; width: 170px; height: 116px;
    background: var(--white);
    display: flex; align-items: center; justify-content: center; text-align: center;
    padding: 0 12px;
    font-size: 20px; font-weight: 500; line-height: 24px; color: var(--band);
  }
  .web {
    position: absolute; left: 201px; top: 210px;
    font-size: 16px; line-height: 22px; color: var(--ink);
  }
  .accent-bar {
    position: absolute; left: 0; right: 0; bottom: 2px; height: 14px; background: var(--lime);
  }
</style>
</head>
<body>
  <div class="ad">
    <div class="ad-inner">
      <div class="brand-mark"></div>
      <div class="brand-name">
        <span class="line">Greta Loxley &amp;</span>
        <span class="line">Nora Loxley Marsh</span>
        <span class="rule"></span>
        <span class="sub">Real Estate</span>
      </div>

      <div class="headline">
        <p class="lead">OPPORTUNITY IS KNOCKING —</p>
        <p class="tag">Let us open the door</p>
      </div>

      <div class="portrait nora" role="img" aria-label="Portrait photo of Nora Loxley"></div>
      <div class="portrait greta" role="img" aria-label="Portrait photo of Greta Loxley"></div>

      <div class="contact-band">
        <p class="agent nora">Nora:<br>(206) 555-0147</p>
        <p class="agent greta">Greta:<br>(206) 555-0182</p>
      </div>

      <div class="info-panel">
        <p class="promise">Your trusted Mercer Island real estate team —<br>providing over 40 years of combined<br>real estate experience</p>
        <div class="broker-badge">Ridgeway Harlan Teague</div>
        <p class="web">info@gretaandnora.com<br>www.gretaandnora.com</p>
      </div>

      <div class="accent-bar"></div>
    </div>
  </div>
</body>
</html>
```